Fleet Wrap - Wall Partitions Company

We are looking for a vehicle/fleet wrap design for Brightfold Panel Works, a company that sells and installs operable/folding wall partitions for commercial spaces. Our systems are used in offices, schools, hotels, conference centers, and other spaces that need flexible room configurations.

The goal of the wrap is to improve brand visibility and recognition while our vehicles are on the road and at job sites. We want the design to feel modern, professional, architectural, and memorable, while making it immediately clear what our company does.

The design should incorporate imagery, graphics, or architectural elements that communicate movable walls, folding partitions, and/or flexible spaces, along with our company colors (see logo attached). As well as display our logo/name, location, and phone number (obtained from our website - brightfoldpanels.example). We are open to creative concepts, but would prefer something clean and distinctive rather than overly busy.

The vehicle we want wrapped, is a KESTA Voyant 2400 (see link here - https://www.kestavans.example/kesta-voyant/specs.2400-cargo-van-high-roof-159-wb.html)

Key priorities:
- Strong brand visibility from a distance
- Contemporary, architectural look
- Clearly communicate that we sell and install folding/operable wall systems
- Easy-to-read company name and website
- Professional enough for commercial construction and corporate clients

```html
<!DOCTYPE html>
<html lang="en">
<head>
<meta charset="utf-8">
<title>Brightfold Panel Works – Fleet Wrap Proof</title>
<link rel="stylesheet" href="https://fonts.googleapis.com/css2?family=Cinzel:wght@400&family=Montserrat:wght@400;500&family=Roboto:wght@400&display=swap">
<style>
  :root{
    --ink:#252525;
    --panel:#2a2a2a;
    --trim:#3a3b3d;
    --body:#ffffff;
    --line:#9a9da2;
    --orange:#f7931e;
    --blue:#1565c0;
    --glass:#8e9297;
    --tail:#c8102e;
    --steel:#cfd2d6;
    --page:#ffffff;
  }
  html,body{margin:0;padding:0;overflow:hidden;background:var(--page);}
  .canvas{display:block;width:1200px;height:800px;}
  .van-body{fill:var(--body);stroke:var(--line);stroke-width:1;}
  .trim{fill:var(--trim);}
  .wrap-panel{fill:var(--panel);}
  .accent-stripe{fill:var(--orange);}
  .glass{fill:var(--glass);stroke:#3a3a3a;stroke-width:2;}
  .tyre{fill:#1d1d1d;}
  .rim{fill:var(--steel);stroke:#666;stroke-width:1;}
  .hub{fill:#444;}
  .tail-light{fill:var(--tail);}
  .brand-square{fill:var(--orange);}
  .brand-name{font-family:"Cinzel",serif;fill:#fff;font-weight:400;}
  .brand-name--dark{fill:var(--ink);}
  .tagline{font-family:"Montserrat",sans-serif;font-weight:400;letter-spacing:2px;font-size:15px;}
  .tagline--light{fill:#fff;}
  .tagline--accent{fill:var(--orange);font-weight:500;}
  .services{font-family:"Roboto",sans-serif;font-size:7px;fill:#fff;}
  .contact{font-family:"Montserrat",sans-serif;font-size:10.5px;fill:var(--ink);font-weight:400;}
  .divider{stroke:var(--blue);stroke-width:1.4;}
  .maker-mark{font-family:"Montserrat",sans-serif;font-weight:500;fill:#fff;letter-spacing:2px;}
</style>
</head>
<body>
<svg class="canvas" viewBox="0 0 1200 800" xmlns="http://www.w3.org/2000/svg">
  <defs>
    <linearGradient id="interior-tones" x1="0" y1="0" x2="0" y2="1">
      <stop offset="0" stop-color="#d9dadc"/>
      <stop offset="0.45" stop-color="#b9a88e"/>
      <stop offset="1" stop-color="#6f7277"/>
    </linearGradient>
    <linearGradient id="glass-tone" x1="0" y1="0" x2="1" y2="1">
      <stop offset="0" stop-color="#b4b7bb"/>
      <stop offset="1" stop-color="#6d7075"/>
    </linearGradient>

    <g id="side-van-shapes">
      <path class="van-body" d="M320,50 L835,50 Q848,52 850,66 L852,326 L40,330 L38,290 Q40,256 72,240 L122,220 L232,108 Q290,54 320,50 Z"/>
      <polygon role="img" aria-label="Office interior with tan folding wall panels partly opened" fill="url(#interior-tones)" points="695,51 835,51 849,66 852,330 552,330"/>
      <polygon class="accent-stripe" points="688,50 700,50 558,340 546,340"/>
      <polygon class="wrap-panel" points="322,51 690,51 590,258 268,258 298,110"/>
      <polygon class="van-body" points="332,258 590,258 571,298 332,298" style="stroke:none"/>
      <polygon class="trim" points="248,300 650,300 650,322 252,322"/>
      <rect class="trim" x="655" y="298" width="195" height="32"/>
      <path class="trim" d="M40,290 Q42,258 72,248 L92,248 L100,332 L40,332 Z"/>
      <path class="trim" d="M100,330 Q104,258 165,255 Q228,258 232,330 Z"/>
      <path class="trim" d="M660,330 Q664,258 725,255 Q788,258 792,330 Z"/>
      <polygon class="glass" fill="url(#glass-tone)" points="248,118 305,116 302,208 222,208"/>
      <polygon class="glass" fill="url(#glass-tone)" points="232,136 242,128 232,208 200,208"/>
      <rect class="trim" x="178" y="170" width="22" height="42" rx="5"/>
      <path fill="var(--blue)" d="M70,238 L120,226 L112,246 L76,250 Z"/>
      <circle class="tyre" cx="162" cy="335" r="46"/>
      <circle class="rim" cx="162" cy="335" r="24"/>
      <circle class="hub" cx="162" cy="335" r="8"/>
      <circle class="tyre" cx="725" cy="335" r="46"/>
      <circle class="rim" cx="725" cy="335" r="24"/>
      <circle class="hub" cx="725" cy="335" r="8"/>
      <rect class="tail-light" x="836" y="190" width="14" height="72" rx="4"/>
    </g>
  </defs>

  <!-- Driver side -->
  <g class="side-view side-view--driver">
    <use href="#side-van-shapes"/>
    <rect class="brand-square" x="348" y="114" width="38" height="38"/>
    <text class="brand-name" x="398" y="138" font-size="22">BRIGHTFOLD</text>
    <text class="brand-name" x="399" y="153" font-size="11" letter-spacing="4">PANEL WORKS</text>
    <text class="tagline tagline--light" x="348" y="193">FLEXIBLE SPACES.</text>
    <text class="tagline tagline--accent" x="348" y="212">ENDLESS POSSIBILITIES.</text>
    <text class="services" x="348" y="237">OPERABLE WALLS</text>
    <line class="divider" x1="413" y1="228" x2="413" y2="240"/>
    <text class="services" x="420" y="237">FOLDING PARTITIONS</text>
    <line class="divider" x1="496" y1="228" x2="496" y2="240"/>
    <text class="services" x="503" y="237">MOVABLE SOLUTIONS</text>
    <text class="contact" x="340" y="283" textLength="140" lengthAdjust="spacingAndGlyphs">brightfoldpanels.example</text>
    <line class="divider" x1="488" y1="273" x2="488" y2="287"/>
    <text class="contact" x="496" y="283" textLength="70" lengthAdjust="spacingAndGlyphs">555-014-2270</text>
  </g>

  <!-- Passenger side -->
  <g class="side-view side-view--passenger">
    <use href="#side-van-shapes" transform="translate(883 368) scale(-1 1)"/>
    <rect class="brand-square" x="257" y="482" width="38" height="38"/>
    <text class="brand-name" x="307" y="506" font-size="22">BRIGHTFOLD</text>
    <text class="brand-name" x="308" y="521" font-size="11" letter-spacing="4">PANEL WORKS</text>
    <text class="tagline tagline--light" x="297" y="561">FLEXIBLE SPACES.</text>
    <text class="tagline tagline--accent" x="297" y="580">ENDLESS POSSIBILITIES.</text>
    <text class="services" x="297" y="604">OPERABLE WALLS</text>
    <line class="divider" x1="365" y1="595" x2="365" y2="607"/>
    <text class="services" x="373" y="604">FOLDING PARTITIONS</text>
    <line class="divider" x1="453" y1="595" x2="453" y2="607"/>
    <text class="services" x="461" y="604">MOVABLE SOLUTIONS</text>
    <text class="contact" x="318" y="651" textLength="140" lengthAdjust="spacingAndGlyphs">brightfoldpanels.example</text>
    <line class="divider" x1="466" y1="641" x2="466" y2="655"/>
    <text class="contact" x="474" y="651" textLength="70" lengthAdjust="spacingAndGlyphs">555-014-2270</text>
  </g>

  <!-- Rear -->
  <g class="rear-view">
    <rect class="trim" x="907" y="52" width="244" height="290" rx="14"/>
    <rect class="van-body" x="925" y="54" width="206" height="256" style="stroke:none"/>
    <polygon class="accent-stripe" points="928,236 1028,270 1128,236 1128,246 1028,282 928,246"/>
    <polygon class="wrap-panel" points="928,62 1128,62 1128,236 1028,270 928,236"/>
    <rect class="trim" x="1000" y="52" width="56" height="14" rx="3"/>
    <rect class="tail-light" x="910" y="188" width="15" height="78" rx="3"/>
    <rect class="tail-light" x="1131" y="188" width="15" height="78" rx="3"/>
    <rect class="brand-square" x="982" y="106" width="20" height="20"/>
    <text class="brand-name" x="1029" y="160" font-size="17" text-anchor="middle">BRIGHTFOLD</text>
    <text class="brand-name" x="1029" y="175" font-size="10" letter-spacing="4" text-anchor="middle">PANEL WORKS</text>
    <line class="divider" x1="966" y1="186" x2="1090" y2="186"/>
    <text class="services" x="1028" y="198" font-size="7.5" text-anchor="middle">OPERABLE WALLS</text>
    <line class="divider" x1="966" y1="204" x2="1090" y2="204"/>
    <text class="services" x="1028" y="213" font-size="7.5" text-anchor="middle">FOLDING PARTITIONS</text>
    <line class="divider" x1="966" y1="219" x2="1090" y2="219"/>
    <text class="services" x="1028" y="228" font-size="7.5" text-anchor="middle">MOVABLE SOLUTIONS</text>
    <circle cx="1028" cy="252" r="8" fill="none" stroke="#cfcfcf" stroke-width="1.5"/>
    <text class="contact" x="940" y="288" font-size="8.5" textLength="110" lengthAdjust="spacingAndGlyphs">brightfoldpanels.example</text>
    <text class="contact" x="940" y="300" font-size="8.5" textLength="56" lengthAdjust="spacingAndGlyphs">555-014-2270</text>
    <rect class="trim" x="907" y="310" width="244" height="28" rx="4"/>
    <rect class="tyre" x="910" y="336" width="30" height="46" rx="8"/>
    <rect class="tyre" x="1118" y="336" width="30" height="46" rx="8"/>
  </g>

  <!-- Front -->
  <g class="front-view">
    <path class="van-body" d="M935,424 L1125,424 Q1150,428 1155,470 L1165,640 L895,640 L905,470 Q910,428 935,424 Z"/>
    <rect class="glass" fill="url(#glass-tone)" x="918" y="470" width="224" height="94" rx="14"/>
    <rect class="trim" x="862" y="522" width="34" height="48" rx="8"/>
    <rect class="trim" x="1164" y="522" width="34" height="48" rx="8"/>
    <path fill="#b9c4d6" stroke="var(--blue)" stroke-width="2" d="M908,580 L955,596 L910,604 Z"/>
    <path fill="#b9c4d6" stroke="var(--blue)" stroke-width="2" d="M1150,580 L1103,596 L1148,604 Z"/>
    <rect class="brand-square" x="966" y="584" width="14" height="14"/>
    <text class="brand-name brand-name--dark" x="986" y="593" font-size="10">BRIGHTFOLD</text>
    <text class="brand-name brand-name--dark" x="987" y="600" font-size="5.5" letter-spacing="2">PANEL WORKS</text>
    <path class="trim" d="M892,620 L1168,620 L1165,720 L895,720 Z"/>
    <rect x="958" y="622" width="142" height="36" rx="4" fill="#2e2f31" stroke="#8d9095" stroke-width="2"/>
    <text class="maker-mark" x="1029" y="645" font-size="12" text-anchor="middle">KESTA</text>
    <rect x="965" y="665" width="128" height="26" fill="#1f1f20"/>
    <circle cx="918" cy="690" r="5" fill="#ddd"/>
    <circle cx="1142" cy="690" r="5" fill="#ddd"/>
    <rect class="tyre" x="896" y="705" width="32" height="44" rx="8"/>
    <rect class="tyre" x="1132" y="705" width="32" height="44" rx="8"/>
  </g>
</svg>
</body>
</html>
```